Design 5 colour schemes for one web page

We are looking for 5 different colour schemes for our product template to create different kinds of colour tone for our web page, it doesn't need to be restructure the layout, just need to provide different color solution.

Please refer to the attached images and take note of the following when you’re working on the design:
(1) Please precisely reproduce the layout. Cannot remove or delete any wordings, components or column shown in the images.
(2) Okay to revise icons, background color or text style as you prefer. But cannot move/delete them.
(3) Provide PSD source files with good layer management. HTML/CSS are not required.
(4) Make reasonable and professional design.

After completion, please send back:
(1) 5 images with 5 different colour schemes.
(2) Related PSD files.

Industry/Entity Type

Management

Number of Pages Required

1 page

Font styles to use
Serif
Sans Serif

Requirements
Must have
• (1) 5 images for the colour schemes.
• (2) 5 PSD source files with good layer management.
Nice to have
• (1) Explanation about your design of the colour schemes.
Should not have
• (1) HTML/CSS code are not required.

```html
<!DOCTYPE html>
<html lang="en">
<head>
<meta charset="utf-8">
<title>Sports Betting – Today</title>
<link href="https://fonts.googleapis.com/css2?family=Nunito+Sans:wght@400;600;700&display=swap" rel="stylesheet">
<style>
:root{
  --accent:#e0842a;
  --accent-soft:#fbe9d6;
  --navy:#16222f;
  --sidebar:#1d2b3a;
  --slate:#2a3b4d;
  --slate-line:#3a4d61;
  --panel-head:#eef1f4;
  --line:#d8dde3;
  --text:#1e2630;
  --white:#fff;
  --sky-top:#0f1924;
  --sky-mid:#1c3146;
  --pitch:#2d5a63;
  --pitch-low:#3f7a74;
}
*{box-sizing:border-box;margin:0;padding:0}
html,body{width:983px;height:1200px;overflow:hidden}
body{font-family:"Nunito Sans",Arial,sans-serif;color:var(--text);font-size:10.5px;position:relative}
svg{flex:none}
.backdrop{position:absolute;inset:0;background:linear-gradient(180deg,var(--sky-top) 0%,var(--sky-mid) 45%,var(--pitch) 78%,var(--pitch-low) 100%)}
.topbar{position:absolute;top:0;left:74px;width:835px;height:62px;color:#fff;font-size:10px}
.toplinks{position:absolute;top:26px;left:0;display:flex;gap:8px;align-items:center}
.toplinks .sep{opacity:.7}
.badge{background:#e0452b;color:#fff;font-size:8px;padding:0 3px;border-radius:2px;margin-left:3px}
.greet{position:absolute;top:24px;left:501px;font-size:10.5px}
.balance{position:absolute;top:15px;left:580px;width:141px;height:30px;border:1px solid var(--accent);display:flex;align-items:center;gap:6px;padding-left:9px;font-size:10.5px;color:#fff}
.signout{position:absolute;top:15px;left:737px;width:98px;height:30px;border:1px solid var(--accent);display:flex;align-items:center;justify-content:center;font-size:10.5px}
.header{position:absolute;top:62px;left:74px;width:835px;height:60px;background:var(--panel-head)}
.brand{position:absolute;left:14px;top:6px;font-size:38px;color:var(--accent);font-weight:400}
.nav{position:absolute;right:0;top:0;height:60px;display:flex;align-items:center;font-size:14px}
.nav a{height:60px;display:flex;align-items:center;padding:0 16px;color:var(--text);text-decoration:none}
.nav a.active{background:var(--accent);color:#fff;position:relative}
.nav a.active::after{content:"";position:absolute;bottom:0;left:50%;margin-left:-5px;border:5px solid transparent;border-bottom-color:#fff}
.nav .results{height:30px;border:1px solid var(--accent);margin:0 15px 0 8px;padding:0 9px;gap:9px}
.subbar{position:absolute;top:122px;left:74px;width:835px;height:34px;background:#fff;display:flex;align-items:center;font-size:11.5px}
.subbar .lang{display:flex;align-items:center;gap:7px;padding-left:17px;width:150px;border-right:1px solid var(--line);height:20px}
.subbar .date{display:flex;align-items:center;gap:9px;padding-left:19px}
.tools{margin-left:auto;display:flex;align-items:center;height:20px;font-size:10.5px}
.tools span{display:flex;align-items:center;gap:4px;padding:0 8px;border-right:1px solid var(--line);height:20px}
.tools span:last-child{border:0;padding-right:10px}
.sidebar{position:absolute;top:156px;left:74px;width:155px;height:1044px;background:var(--sidebar);color:#fff}
.fav-title{text-align:center;font-size:12px;margin-top:9px;letter-spacing:.3px}
.fav-box{margin:5px 1px 0;height:36px;border:1px solid var(--accent);font-size:9px;text-align:center;line-height:12.5px;padding-top:5px}
.tabs{display:flex;height:32px;margin-top:10px;font-size:12px}
.tabs div{flex:1;display:flex;align-items:center;justify-content:center}
.tabs .on{background:var(--accent)}
.tabs .off{background:var(--navy)}
.sports{list-style:none}
.sports li{height:34.4px;background:var(--slate);border-bottom:1px solid var(--slate-line);display:flex;align-items:center;font-size:9.5px;padding:0 9px 0 13px}
.sports li svg{margin-right:15px}
.sports li .n{margin-left:auto}
.tabs.ticket{margin-top:0;height:31px}
.mybets{text-align:center;padding-top:15px;height:113px}
.mybets h3{font-weight:400;font-size:12px}
.refresh{display:flex;justify-content:center;align-items:center;gap:7px;font-size:9.5px;margin-top:12px}
.pending{margin:13px auto 0;width:100px;height:20px;border:1px solid var(--accent);font-size:9.5px;display:flex;align-items:center;justify-content:center}
.viewall{background:var(--accent);height:30px;display:flex;align-items:center;justify-content:center;font-size:12px}
.copy{text-align:center;font-size:9.5px;line-height:20px;padding-top:13px}
.panel{position:absolute;left:238px;width:671px;background:#fff}
.panel.live{top:164px}
.panel.notlive{top:303px}
.phead{height:26px;background:var(--panel-head);display:flex;align-items:center;color:var(--accent);font-size:12px;position:relative;padding-left:6px}
.phead .title{display:flex;align-items:center;gap:7px}
.phead .count{position:absolute;left:315px;display:flex;align-items:center;gap:6px}
.phead .league{position:absolute;right:16px;display:flex;align-items:center;gap:8px}
.grid{display:grid;grid-template-columns:61px 136px 57px 55px 53px 57px 59px 75px 75px 43px}
.colhead{height:42px;grid-template-rows:21px 21px;font-size:11.5px;border-bottom:1px solid var(--line)}
.colhead div{display:flex;align-items:center;justify-content:center;border-right:1px solid var(--line)}
.colhead .r2{border-top:1px solid var(--line)}
.colhead .span2{grid-row:span 2}
.colhead .more{border-right:0;font-size:10.5px}
.lbar{height:17.5px;background:var(--accent);color:#fff;display:flex;align-items:center;font-size:11px;padding:0 20px 0 8px;gap:10px}
.lbar .rf{margin-left:auto}
.row{height:49px;border-bottom:1px solid var(--line);font-size:10.5px;color:var(--accent)}
.live .row{height:43px;border-bottom:0}
.row>div{display:flex;align-items:center;color:var(--text)}
.row .t{border-right:1px solid var(--line);gap:7px;padding-left:4px}
.row .t svg{color:var(--accent)}
.row .t .tm{text-align:center;line-height:12px;font-size:10px}
.row .ev{border-right:1px solid var(--line);padding-left:6px;gap:6px;line-height:15px}
.row .num{justify-content:center;line-height:17px;text-align:center}
.row .top{align-items:flex-start;padding-top:9px}
.row .ou{border-right:1px solid var(--line);padding-left:12px;line-height:15px}
.row .fh{grid-column:span 3;border-right:1px solid var(--line)}
.row .more{justify-content:center;gap:3px;font-size:11.5px}
.row .more svg{color:var(--accent)}
.footer{position:absolute;top:1119px;left:238px;width:671px;text-align:center;color:#fff;font-size:9.5px;word-spacing:1px}
.footer span{margin:0 6px}
</style>
</head>
<body>
<div class="backdrop" role="img" aria-label="Floodlit football stadium with a pitch at night"></div>

<div class="topbar">
  <div class="toplinks"><span>My Bets</span><span class="sep">|</span><span>Statement</span><span class="sep">|</span><span>Preferences</span><span class="sep">|</span><span>Announcments<span class="badge">99+</span></span></div>
  <div class="greet">Hi, Player027</div>
  <div class="balance">&gt;&gt; <span>SD$</span><span>10,072.00</span>
    <svg width="14" height="14" viewBox="0 0 16 16"><path d="M13 6A5.5 5.5 0 0 0 3 5M3 10a5.5 5.5 0 0 0 10 1" fill="none" stroke="#fff" stroke-width="2"/><path d="M13 1v5h-5M3 15v-5h5" fill="#fff"/></svg></div>
  <div class="signout">Sign Out</div>
</div>

<header class="header">
  <div class="brand">Logo</div>
  <nav class="nav">
    <a>Home</a><a class="active">Sports</a><a>Live Sports</a><a>Live Casino</a>
    <a class="results"><svg width="12" height="14" viewBox="0 0 12 14"><rect x="1" y="1" width="10" height="12" fill="none" stroke="#333"/><path d="M3 10h6M3 4h3" stroke="#333"/></svg>Results</a>
  </nav>
</header>

<div class="subbar">
  <div class="lang"><svg width="16" height="16" viewBox="0 0 16 16"><circle cx="8" cy="8" r="7" fill="none" stroke="#333" stroke-width="1.3"/><path d="M1 8h14M8 1c-3 3-3 11 0 14M8 1c3 3 3 11 0 14" fill="none" stroke="#333"/></svg>English (Asia)</div>
  <div class="date"><svg width="17" height="17" viewBox="0 0 17 17"><rect x="1" y="3" width="15" height="13" fill="none" stroke="#333" stroke-width="1.4"/><path d="M1 7h15M5 1v4M12 1v4M4 10h2M8 10h2M12 10h1M4 13h2M8 13h2" stroke="#333" stroke-width="1.4"/></svg>Nov, 19, 2014 11 : 40 AM</div>
  <div class="tools">
    <span><svg width="18" height="16" viewBox="0 0 18 16"><rect x="1" y="1" width="12" height="13" fill="none" stroke="#333" stroke-width="1.3"/><path d="M3 5h8M3 8h5" stroke="#333"/><circle cx="13" cy="11" r="4" fill="#fff" stroke="#333"/><path d="M13 9v4M11 11h4" stroke="#333"/></svg><svg width="8" height="5"><path d="M0 0h8L4 5z" fill="#333"/></svg></span>
    <span><svg width="14" height="13" viewBox="0 0 24 23"><path d="M12 0l3.5 7.5 8 1-6 5.5 1.7 8L12 18l-7.2 4 1.7-8-6-5.5 8-1z" fill="#333"/></svg><svg width="8" height="5"><path d="M0 0h8L4 5z" fill="#333"/></svg></span>
    <span>My<svg width="8" height="5"><path d="M0 0h8L4 5z" fill="#333"/></svg></span>
    <span><svg width="16" height="14" viewBox="0 0 16 14"><path d="M1 5h3l4-4v12L4 9H1z" fill="#333"/><path d="M10 4q2 3 0 6M12 2q4 5 0 10" fill="none" stroke="#333" stroke-width="1.3"/></svg></span>
    <span><svg width="20" height="18" viewBox="0 0 20 18"><rect x="1" y="5" width="18" height="12" fill="none" stroke="#333" stroke-width="1.5"/><path d="M6 1l4 4 4-4" fill="none" stroke="#333" stroke-width="1.3"/></svg></span>
    <span>Live</span>
  </div>
</div>

<aside class="sidebar">
  <div class="fav-title">MY FAVOURITES</div>
  <div class="fav-box">Click An Event Or League<br>To Add It To "My Favourites"</div>
  <div class="tabs"><div class="on">SPORTS</div><div class="off">MARKETS</div></div>
  <ul class="sports">
    <li><svg width="14" height="14"><circle cx="7" cy="7" r="5" fill="none" stroke="#fff" stroke-width="1.5"/></svg>Football<span class="n">600</span></li>
    <li><svg width="14" height="14"><circle cx="7" cy="7" r="5" fill="none" stroke="#fff" stroke-width="1.5"/></svg>Basketball<span class="n">600</span></li>
    <li><svg width="14" height="14"><circle cx="7" cy="7" r="5" fill="none" stroke="#fff" stroke-width="1.5"/></svg>Baseball<span class="n">600</span></li>
    <li><svg width="14" height="14"><circle cx="7" cy="7" r="5" fill="none" stroke="#fff" stroke-width="1.5"/></svg>Tennis<span class="n">600</span></li>
    <li><svg width="14" height="14"><circle cx="7" cy="7" r="5" fill="none" stroke="#fff" stroke-width="1.5"/></svg>US Football<span class="n">600</span></li>
    <li><svg width="14" height="14"><circle cx="7" cy="7" r="5" fill="none" stroke="#fff" stroke-width="1.5"/></svg>Badminton<span class="n">600</span></li>
    <li><svg width="14" height="14"><circle cx="7" cy="7" r="5" fill="none" stroke="#fff" stroke-width="1.5"/></svg>Boxing<span class="n">600</span></li>
    <li><svg width="14" height="14"><circle cx="7" cy="7" r="5" fill="none" stroke="#fff" stroke-width="1.5"/></svg>Cricket<span class="n">600</span></li>
    <li><svg width="14" height="14"><circle cx="7" cy="7" r="5" fill="none" stroke="#fff" stroke-width="1.5"/></svg>Cycling<span class="n">600</span></li>
    <li><svg width="14" height="14"><circle cx="7" cy="7" r="5" fill="none" stroke="#fff" stroke-width="1.5"/></svg>Darts<span class="n">600</span></li>
    <li><svg width="14" height="14"><circle cx="7" cy="7" r="5" fill="none" stroke="#fff" stroke-width="1.5"/></svg>Entertainment<span class="n">600</span></li>
    <li><svg width="14" height="14"><circle cx="7" cy="7" r="5" fill="none" stroke="#fff" stroke-width="1.5"/></svg>Golf<span class="n">600</span></li>
    <li><svg width="14" height="14"><circle cx="7" cy="7" r="5" fill="none" stroke="#fff" stroke-width="1.5"/></svg>Handball<span class="n">600</span></li>
    <li><svg width="14" height="14"><circle cx="7" cy="7" r="5" fill="none" stroke="#fff" stroke-width="1.5"/></svg>Ice Hockey<span class="n">600</span></li>
    <li><svg width="14" height="14"><circle cx="7" cy="7" r="5" fill="none" stroke="#fff" stroke-width="1.5"/></svg>Martial Arts<span class="n">600</span></li>
    <li><svg width="14" height="14"><circle cx="7" cy="7" r="5" fill="none" stroke="#fff" stroke-width="1.5"/></svg>Motor Sports<span class="n">600</span></li>
    <li><svg width="14" height="14"><circle cx="7" cy="7" r="5" fill="none" stroke="#fff" stroke-width="1.5"/></svg>Snooker<span class="n">600</span></li>
    <li><svg width="14" height="14"><circle cx="7" cy="7" r="5" fill="none" stroke="#fff" stroke-width="1.5"/></svg>Rugby<span class="n">600</span></li>
    <li><svg width="14" height="14"><circle cx="7" cy="7" r="5" fill="none" stroke="#fff" stroke-width="1.5"/></svg>Voleyball<span class="n">600</span></li>
    <li><svg width="14" height="14"><circle cx="7" cy="7" r="5" fill="none" stroke="#fff" stroke-width="1.5"/></svg>Winter Sports<span class="n">600</span></li>
  </ul>
  <div class="tabs ticket"><div class="on">TICKET</div><div class="off">PARLAY 0</div></div>
  <div class="mybets">
    <h3>MY BETS</h3>
    <div class="refresh"><svg width="15" height="15" viewBox="0 0 16 16"><path d="M13 6A5.5 5.5 0 0 0 3 5M3 10a5.5 5.5 0 0 0 10 1" fill="none" stroke="#fff" stroke-width="2"/><path d="M13 1v5h-5M3 15v-5h5" fill="#fff"/></svg>REFRESH</div>
    <div class="pending">No Pending Bets</div>
  </div>
  <div class="viewall">VIEW ALL</div>
  <div class="copy">© 2014 - Betting<br>All Rights Reserved.</div>
</aside>

<section class="panel live">
  <div class="phead">
    <div class="title"><svg width="12" height="14" viewBox="0 0 12 14"><circle cx="7" cy="2" r="1.8" fill="currentColor"/><path d="M6 5L4 9l3 1-1 4M6 5l3 3M6 5L2 7M4 9L2 13" stroke="currentColor" stroke-width="1.6" fill="none"/></svg>TODAY LIVE</div>
    <div class="count"><svg width="15" height="15" viewBox="0 0 16 16"><path d="M13 6A5.5 5.5 0 0 0 3 5M3 10a5.5 5.5 0 0 0 10 1" fill="none" stroke="currentColor" stroke-width="2"/><path d="M13 1v5h-5M3 15v-5h5" fill="currentColor"/></svg>38</div>
    <div class="league"><svg width="12" height="14" viewBox="0 0 12 14"><path d="M1 1h10v3a5 5 0 0 1-10 0zM5 9h2v3h2v2H3v-2h2z" fill="currentColor"/></svg>Select League<svg width="9" height="5"><path d="M0 0h9L4.5 5z" fill="currentColor"/></svg></div>
  </div>
  <div class="grid colhead">
    <div class="span2">Time</div><div class="span2">Events</div>
    <div style="grid-column:span 4">Full Time</div><div style="grid-column:span 3">First Half</div>
    <div class="span2 more">+More</div>
    <div class="r2">A 1×2</div><div class="r2">HDP</div><div class="r2">OU</div><div class="r2">1×2</div><div class="r2">HDP</div><div class="r2">OU</div><div class="r2">1×2</div>
  </div>
  <div class="lbar"><svg width="11" height="11" viewBox="0 0 24 23"><path d="M12 0l3.5 7.5 8 1-6 5.5 1.7 8L12 18l-7.2 4 1.7-8-6-5.5 8-1z" fill="#fff"/></svg>Coastal Premier League<svg class="rf" width="15" height="14" viewBox="0 0 16 16"><path d="M13 6A5.5 5.5 0 0 0 3 5M3 10a5.5 5.5 0 0 0 10 1" fill="none" stroke="#fff" stroke-width="2"/><path d="M13 1v5h-5M3 15v-5h5" fill="#fff"/></svg></div>
  <div class="grid row"><div class="t"><svg width="14" height="12"><path d="M1 11V6M5 11V3M9 11V7M13 11V1" stroke="currentColor" stroke-width="2"/></svg><div class="tm">16 : 30<br>Live</div></div><div class="ev"><svg width="9" height="9" viewBox="0 0 24 23"><path d="M12 0l3.5 7.5 8 1-6 5.5 1.7 8L12 18l-7.2 4 1.7-8-6-5.5 8-1z" fill="#222"/></svg><div>Bayside Anchors FC<br>Southgate Comets</div></div><div class="num">0-0.5</div><div class="num">0.77<br>-0.95</div><div class="num top">6-6.5</div><div class="ou">O&nbsp; -0.85<br>U&nbsp; -0.65</div><div class="fh"></div><div class="more"><svg width="9" height="13"><path d="M4.5 0L9 5.5H0zM4.5 13L0 7.5h9z" fill="currentColor"/></svg>13</div></div>
</section>

<section class="panel notlive">
  <div class="phead">
    <div class="title"><svg width="12" height="14" viewBox="0 0 12 14"><circle cx="7" cy="2" r="1.8" fill="currentColor"/><path d="M6 5L4 9l3 1-1 4M6 5l3 3M6 5L2 7M4 9L2 13" stroke="currentColor" stroke-width="1.6" fill="none"/></svg>TODAY NOT LIVE</div>
    <div class="count"><svg width="15" height="15" viewBox="0 0 16 16"><path d="M13 6A5.5 5.5 0 0 0 3 5M3 10a5.5 5.5 0 0 0 10 1" fill="none" stroke="currentColor" stroke-width="2"/><path d="M13 1v5h-5M3 15v-5h5" fill="currentColor"/></svg>38</div>
    <div class="league" style="right:26px"><svg width="12" height="14" viewBox="0 0 12 14"><path d="M1 1h10v3a5 5 0 0 1-10 0zM5 9h2v3h2v2H3v-2h2z" fill="currentColor"/></svg>Select League<svg width="9" height="5"><path d="M0 0h9L4.5 5z" fill="currentColor"/></svg></div>
  </div>
  <div class="grid colhead">
    <div class="span2">Time</div><div class="span2">Events</div>
    <div style="grid-column:span 4">Full Time</div><div style="grid-column:span 3">First Half</div>
    <div class="span2 more">+More</div>
    <div class="r2">A 1×2</div><div class="r2">HDP</div><div class="r2">OU</div><div class="r2">1×2</div><div class="r2">HDP</div><div class="r2">OU</div><div class="r2">1×2</div>
  </div>

  <div class="lbar"><svg width="11" height="11" viewBox="0 0 24 23"><path d="M12 0l3.5 7.5 8 1-6 5.5 1.7 8L12 18l-7.2 4 1.7-8-6-5.5 8-1z" fill="#fff"/></svg>Coastal Premier League<svg class="rf" width="15" height="14" viewBox="0 0 16 16"><path d="M13 6A5.5 5.5 0 0 0 3 5M3 10a5.5 5.5 0 0 0 10 1" fill="none" stroke="#fff" stroke-width="2"/><path d="M13 1v5h-5M3 15v-5h5" fill="#fff"/></svg></div>
  <div class="grid row"><div class="t"><svg width="14" height="12"><path d="M1 11V6M5 11V3M9 11V7M13 11V1" stroke="currentColor" stroke-width="2"/></svg><div class="tm">16 : 30<br>Live</div></div><div class="ev"><svg width="9" height="9" viewBox="0 0 24 23"><path d="M12 0l3.5 7.5 8 1-6 5.5 1.7 8L12 18l-7.2 4 1.7-8-6-5.5 8-1z" fill="#222"/></svg><div>Bayside Anchors FC<br>Southgate Comets</div></div><div class="num">0-0.5</div><div class="num">0.77<br>-0.95</div><div class="num top">6-6.5</div><div class="ou">O&nbsp; -0.85<br>U&nbsp; -0.65</div><div class="fh"></div><div class="more"><svg width="9" height="13"><path d="M4.5 0L9 5.5H0zM4.5 13L0 7.5h9z" fill="currentColor"/></svg>13</div></div>

  <div class="lbar"><svg width="11" height="11" viewBox="0 0 24 23"><path d="M12 0l3.5 7.5 8 1-6 5.5 1.7 8L12 18l-7.2 4 1.7-8-6-5.5 8-1z" fill="#fff"/></svg>Coastal Premier League<svg class="rf" width="15" height="14" viewBox="0 0 16 16"><path d="M13 6A5.5 5.5 0 0 0 3 5M3 10a5.5 5.5 0 0 0 10 1" fill="none" stroke="#fff" stroke-width="2"/><path d="M13 1v5h-5M3 15v-5h5" fill="#fff"/></svg></div>
  <div class="grid row"><div class="t"><svg width="14" height="12"><path d="M1 11V6M5 11V3M9 11V7M13 11V1" stroke="currentColor" stroke-width="2"/></svg><div class="tm">16 : 30<br>Live</div></div><div class="ev"><svg width="9" height="9" viewBox="0 0 24 23"><path d="M12 0l3.5 7.5 8 1-6 5.5 1.7 8L12 18l-7.2 4 1.7-8-6-5.5 8-1z" fill="#222"/></svg><div>Bayside Anchors FC<br>Southgate Comets</div></div><div class="num">0-0.5</div><div class="num">0.77<br>-0.95</div><div class="num top">6-6.5</div><div class="ou">O&nbsp; -0.85<br>U&nbsp; -0.65</div><div class="fh"></div><div class="more"><svg width="9" height="13"><path d="M4.5 0L9 5.5H0zM4.5 13L0 7.5h9z" fill="currentColor"/></svg>13</div></div>
  <div class="grid row"><div class="t"><svg width="14" height="12"><path d="M1 11V6M5 11V3M9 11V7M13 11V1" stroke="currentColor" stroke-width="2"/></svg><div class="tm">16 : 30<br>Live</div></div><div class="ev"><svg width="9" height="9" viewBox="0 0 24 23"><path d="M12 0l3.5 7.5 8 1-6 5.5 1.7 8L12 18l-7.2 4 1.7-8-6-5.5 8-1z" fill="#222"/></svg><div>Bayside Anchors FC<br>Southgate Comets</div></div><div class="num">0-0.5</div><div class="num">0.77<br>-0.95</div><div class="num top">6-6.5</div><div class="ou">O&nbsp; -0.85<br>U&nbsp; -0.65</div><div class="fh"></div><div class="more"><svg width="9" height="13"><path d="M4.5 0L9 5.5H0zM4.5 13L0 7.5h9z" fill="currentColor"/></svg>13</div></div>
  <div class="grid row"><div class="t"><svg width="14" height="12"><path d="M1 11V6M5 11V3M9 11V7M13 11V1" stroke="currentColor" stroke-width="2"/></svg><div class="tm">16 : 30<br>Live</div></div><div class="ev"><svg width="9" height="9" viewBox="0 0 24 23"><path d="M12 0l3.5 7.5 8 1-6 5.5 1.7 8L12 18l-7.2 4 1.7-8-6-5.5 8-1z" fill="#222"/></svg><div>Bayside Anchors FC<br>Southgate Comets</div></div><div class="num">0-0.5</div><div class="num">0.77<br>-0.95</div><div class="num top">6-6.5</div><div class="ou">O&nbsp; -0.85<br>U&nbsp; -0.65</div><div class="fh"></div><div class="more"><svg width="9" height="13"><path d="M4.5 0L9 5.5H0zM4.5 13L0 7.5h9z" fill="currentColor"/></svg>13</div></div>

  <div class="lbar"><svg width="11" height="11" viewBox="0 0 24 23"><path d="M12 0l3.5 7.5 8 1-6 5.5 1.7 8L12 18l-7.2 4 1.7-8-6-5.5 8-1z" fill="#fff"/></svg>Coastal Premier League<svg class="rf" width="15" height="14" viewBox="0 0 16 16"><path d="M13 6A5.5 5.5 0 0 0 3 5M3 10a5.5 5.5 0 0 0 10 1" fill="none" stroke="#fff" stroke-width="2"/><path d="M13 1v5h-5M3 15v-5h5" fill="#fff"/></svg></div>
  <div class="grid row"><div class="t"><svg width="14" height="12"><path d="M1 11V6M5 11V3M9 11V7M13 11V1" stroke="currentColor" stroke-width="2"/></svg><div class="tm">16 : 30<br>Live</div></div><div class="ev"><svg width="9" height="9" viewBox="0 0 24 23"><path d="M12 0l3.5 7.5 8 1-6 5.5 1.7 8L12 18l-7.2 4 1.7-8-6-5.5 8-1z" fill="#222"/></svg><div>Bayside Anchors FC<br>Southgate Comets</div></div><div class="num">0-0.5</div><div class="num">0.77<br>-0.95</div><div class="num top">6-6.5</div><div class="ou">O&nbsp; -0.85<br>U&nbsp; -0.65</div><div class="fh"></div><div class="more"><svg width="9" height="13"><path d="M4.5 0L9 5.5H0zM4.5 13L0 7.5h9z" fill="currentColor"/></svg>13</div></div>

  <div class="lbar"><svg width="11" height="11" viewBox="0 0 24 23"><path d="M12 0l3.5 7.5 8 1-6 5.5 1.7 8L12 18l-7.2 4 1.7-8-6-5.5 8-1z" fill="#fff"/></svg>Coastal Premier League<svg class="rf" width="15" height="14" viewBox="0 0 16 16"><path d="M13 6A5.5 5.5 0 0 0 3 5M3 10a5.5 5.5 0 0 0 10 1" fill="none" stroke="#fff" stroke-width="2"/><path d="M13 1v5h-5M3 15v-5h5" fill="#fff"/></svg></div>
  <div class="grid row"><div class="t"><svg width="14" height="12"><path d="M1 11V6M5 11V3M9 11V7M13 11V1" stroke="currentColor" stroke-width="2"/></svg><div class="tm">16 : 30<br>Live</div></div><div class="ev"><svg width="9" height="9" viewBox="0 0 24 23"><path d="M12 0l3.5 7.5 8 1-6 5.5 1.7 8L12 18l-7.2 4 1.7-8-6-5.5 8-1z" fill="#222"/></svg><div>Bayside Anchors FC<br>Southgate Comets</div></div><div class="num">0-0.5</div><div class="num">0.77<br>-0.95</div><div class="num top">6-6.5</div><div class="ou">O&nbsp; -0.85<br>U&nbsp; -0.65</div><div class="fh"></div><div class="more"><svg width="9" height="13"><path d="M4.5 0L9 5.5H0zM4.5 13L0 7.5h9z" fill="currentColor"/></svg>13</div></div>
  <div class="grid row"><div class="t"><svg width="14" height="12"><path d="M1 11V6M5 11V3M9 11V7M13 11V1" stroke="currentColor" stroke-width="2"/></svg><div class="tm">16 : 30<br>Live</div></div><div class="ev"><svg width="9" height="9" viewBox="0 0 24 23"><path d="M12 0l3.5 7.5 8 1-6 5.5 1.7 8L12 18l-7.2 4 1.7-8-6-5.5 8-1z" fill="#222"/></svg><div>Bayside Anchors FC<br>Southgate Comets</div></div><div class="num">0-0.5</div><div class="num">0.77<br>-0.95</div><div class="num top">6-6.5</div><div class="ou">O&nbsp; -0.85<br>U&nbsp; -0.65</div><div class="fh"></div><div class="more"><svg width="9" height="13"><path d="M4.5 0L9 5.5H0zM4.5 13L0 7.5h9z" fill="currentColor"/></svg>13</div></div>
  <div class="grid row"><div class="t"><svg width="14" height="12"><path d="M1 11V6M5 11V3M9 11V7M13 11V1" stroke="currentColor" stroke-width="2"/></svg><div class="tm">16 : 30<br>Live</div></div><div class="ev"><svg width="9" height="9" viewBox="0 0 24 23"><path d="M12 0l3.5 7.5 8 1-6 5.5 1.7 8L12 18l-7.2 4 1.7-8-6-5.5 8-1z" fill="#222"/></svg><div>Bayside Anchors FC<br>Southgate Comets</div></div><div class="num">0-0.5</div><div class="num">0.77<br>-0.95</div><div class="num top">6-6.5</div><div class="ou">O&nbsp; -0.85<br>U&nbsp; -0.65</div><div class="fh"></div><div class="more"><svg width="9" height="13"><path d="M4.5 0L9 5.5H0zM4.5 13L0 7.5h9z" fill="currentColor"/></svg>13</div></div>
  <div class="grid row"><div class="t"><svg width="14" height="12"><path d="M1 11V6M5 11V3M9 11V7M13 11V1" stroke="currentColor" stroke-width="2"/></svg><div class="tm">16 : 30<br>Live</div></div><div class="ev"><svg width="9" height="9" viewBox="0 0 24 23"><path d="M12 0l3.5 7.5 8 1-6 5.5 1.7 8L12 18l-7.2 4 1.7-8-6-5.5 8-1z" fill="#222"/></svg><div>Bayside Anchors FC<br>Southgate Comets</div></div><div class="num">0-0.5</div><div class="num">0.77<br>-0.95</div><div class="num top">6-6.5</div><div class="ou">O&nbsp; -0.85<br>U&nbsp; -0.65</div><div class="fh"></div><div class="more"><svg width="9" height="13"><path d="M4.5 0L9 5.5H0zM4.5 13L0 7.5h9z" fill="currentColor"/></svg>13</div></div>
  <div class="grid row"><div class="t"><svg width="14" height="12"><path d="M1 11V6M5 11V3M9 11V7M13 11V1" stroke="currentColor" stroke-width="2"/></svg><div class="tm">16 : 30<br>Live</div></div><div class="ev"><svg width="9" height="9" viewBox="0 0 24 23"><path d="M12 0l3.5 7.5 8 1-6 5.5 1.7 8L12 18l-7.2 4 1.7-8-6-5.5 8-1z" fill="#222"/></svg><div>Bayside Anchors FC<br>Southgate Comets</div></div><div class="num">0-0.5</div><div class="num">0.77<br>-0.95</div><div class="num top">6-6.5</div><div class="ou">O&nbsp; -0.85<br>U&nbsp; -0.65</div><div class="fh"></div><div class="more"><svg width="9" height="13"><path d="M4.5 0L9 5.5H0zM4.5 13L0 7.5h9z" fill="currentColor"/></svg>13</div></div>
  <div class="grid row"><div class="t"><svg width="14" height="12"><path d="M1 11V6M5 11V3M9 11V7M13 11V1" stroke="currentColor" stroke-width="2"/></svg><div class="tm">16 : 30<br>Live</div></div><div class="ev"><svg width="9" height="9" viewBox="0 0 24 23"><path d="M12 0l3.5 7.5 8 1-6 5.5 1.7 8L12 18l-7.2 4 1.7-8-6-5.5 8-1z" fill="#222"/></svg><div>Bayside Anchors FC<br>Southgate Comets</div></div><div class="num">0-0.5</div><div class="num">0.77<br>-0.95</div><div class="num top">6-6.5</div><div class="ou">O&nbsp; -0.85<br>U&nbsp; -0.65</div><div class="fh"></div><div class="more"><svg width="9" height="13"><path d="M4.5 0L9 5.5H0zM4.5 13L0 7.5h9z" fill="currentColor"/></svg>13</div></div>
  <div class="grid row"><div class="t"><svg width="14" height="12"><path d="M1 11V6M5 11V3M9 11V7M13 11V1" stroke="currentColor" stroke-width="2"/></svg><div class="tm">16 : 30<br>Live</div></div><div class="ev"><svg width="9" height="9" viewBox="0 0 24 23"><path d="M12 0l3.5 7.5 8 1-6 5.5 1.7 8L12 18l-7.2 4 1.7-8-6-5.5 8-1z" fill="#222"/></svg><div>Bayside Anchors FC<br>Southgate Comets</div></div><div class="num">0-0.5</div><div class="num">0.77<br>-0.95</div><div class="num top">6-6.5</div><div class="ou">O&nbsp; -0.85<br>U&nbsp; -0.65</div><div class="fh"></div><div class="more"><svg width="9" height="13"><path d="M4.5 0L9 5.5H0zM4.5 13L0 7.5h9z" fill="currentColor"/></svg>13</div></div>
  <div class="grid row"><div class="t"><svg width="14" height="12"><path d="M1 11V6M5 11V3M9 11V7M13 11V1" stroke="currentColor" stroke-width="2"/></svg><div class="tm">16 : 30<br>Live</div></div><div class="ev"><svg width="9" height="9" viewBox="0 0 24 23"><path d="M12 0l3.5 7.5 8 1-6 5.5 1.7 8L12 18l-7.2 4 1.7-8-6-5.5 8-1z" fill="#222"/></svg><div>Bayside Anchors FC<br>Southgate Comets</div></div><div class="num">0-0.5</div><div class="num">0.77<br>-0.95</div><div class="num top">6-6.5</div><div class="ou">O&nbsp; -0.85<br>U&nbsp; -0.65</div><div class="fh"></div><div class="more"><svg width="9" height="13"><path d="M4.5 0L9 5.5H0zM4.5 13L0 7.5h9z" fill="currentColor"/></svg>13</div></div>
</section>

<footer class="footer">Betting Rules<span>|</span>Contact Us<span>|</span>Privacy Policy<span>|</span>Responsible Gambling<span>|</span>Terms &amp; Conditions<span>|</span>Tutorials</footer>
</body>
</html>
```